PROPERTY MANAGEMENT AND REAL ESTATE

Target Market(s)

real estate owners and investors

Industry/Entity Type

Real Estate

Contact Information for Business Card

BRIGHT LANTERN PROPERTY MANAGEMENT GROUP, LLC
487 North Corwin Parkway
Suite 260
Marlow Springs, FL 33127

```html
<!DOCTYPE html>
<html lang="en">
<head>
<meta charset="utf-8">
<title>Bright Lantern Property Management Group – Business Card</title>
<link rel="stylesheet" href="https://fonts.googleapis.com/css2?family=Open+Sans:wght@300;400;600;700&display=swap">
<style>
  :root {
    --red: #c8202e;
    --red-dark: #8f1620;
    --red-light: #d94552;
    --ink: #3a3a3a;
    --muted: #7a7a7a;
    --paper: #ffffff;
    --backdrop: #ecebe9;
  }
  * { box-sizing: border-box; margin: 0; padding: 0; }
  html, body {
    width: 1200px; height: 800px; overflow: hidden;
    background: var(--backdrop);
    font-family: "Open Sans", Arial, sans-serif;
  }
  .stage {
    width: 1200px; height: 800px;
    display: flex; align-items: center; justify-content: center; gap: 40px;
  }
  .card {
    position: relative; width: 540px; height: 309px; overflow: hidden;
    box-shadow: 0 6px 18px rgba(0,0,0,.18);
  }

  /* Back side */
  .card-back {
    background: linear-gradient(135deg, var(--red-light) 0%, var(--red) 55%, var(--red-dark) 100%);
    color: #fff;
  }
  .back-company {
    position: absolute; left: 44px; top: 44px;
    font-weight: 300; font-size: 27px; line-height: 1.2; letter-spacing: .5px;
    text-transform: uppercase;
  }
  .back-web {
    position: absolute; left: 46px; top: 128px;
    font-size: 14px; opacity: .85;
  }

  /* Front side */
  .card-front { background: var(--paper); }
  .brand { position: absolute; left: 34px; top: 30px; display: flex; align-items: center; gap: 16px; }
  .brand-mark { width: 62px; height: 62px; border-radius: 50%; background: var(--red); }
  .brand-name {
    font-weight: 400; font-size: 16px; line-height: 1.2; color: var(--ink);
    text-transform: uppercase; letter-spacing: .3px;
  }
  .person { position: absolute; left: 34px; top: 108px; }
  .person-name { font-weight: 700; font-size: 19px; color: var(--red); text-transform: uppercase; }
  .person-title { font-size: 11px; color: var(--muted); margin-top: 2px; }
  .contacts { position: absolute; right: 40px; top: 150px; list-style: none; }
  .contacts li { display: flex; align-items: center; gap: 8px; font-size: 13.5px; color: var(--ink); line-height: 1.55; }
  .contacts svg { width: 12px; height: 12px; flex: none; }
  .address-band {
    position: absolute; left: 0; bottom: 0; width: 100%; height: 62px;
  }
  .address {
    position: absolute; left: 22px; bottom: 15px;
    font-size: 13px; color: #fff; letter-spacing: .2px;
  }
</style>
</head>
<body>
<main class="stage">
  <section class="card card-back" aria-label="Back of business card">
    <h1 class="back-company">Bright Lantern Property<br>Management Group, LLC</h1>
    <p class="back-web">www.brightlanternpm.com</p>
  </section>

  <section class="card card-front" aria-label="Front of business card">
    <div class="brand">
      <span class="brand-mark" aria-hidden="true"></span>
      <p class="brand-name">Bright Lantern Property<br>Management Group, LLC</p>
    </div>
    <div class="person">
      <p class="person-name">Daniel Halvorsen</p>
      <p class="person-title">Director</p>
    </div>
    <ul class="contacts">
      <li>
        <svg viewBox="0 0 12 12" aria-hidden="true"><rect width="12" height="12" fill="var(--red)"/><path d="M3.5 2.5l1.3 1.8-.7.9c.5 1 1.3 1.8 2.3 2.3l.9-.7 1.8 1.3-.8 1.4C5.6 9.2 2.8 6.4 2.5 3.3z" fill="#fff"/></svg>
        305-555-0148
      </li>
      <li>
        <svg viewBox="0 0 12 12" aria-hidden="true"><rect width="12" height="12" fill="var(--red)"/><rect x="4" y="2" width="4" height="8" rx=".6" fill="#fff"/><rect x="4.8" y="3" width="2.4" height="4.5" fill="var(--red)"/></svg>
        786-555-0193
      </li>
      <li>
        <svg viewBox="0 0 12 12" aria-hidden="true"><rect width="12" height="12" fill="var(--red)"/><rect x="2.5" y="3.5" width="7" height="5" fill="#fff"/><path d="M2.5 3.5L6 6.3l3.5-2.8" fill="none" stroke="var(--red)" stroke-width=".8"/></svg>
        daniel@brightlanternpm.com
      </li>
    </ul>
    <svg class="address-band" viewBox="0 0 540 62" preserveAspectRatio="none" aria-hidden="true">
      <polygon points="0,12 470,12 490,32 540,32 540,36 488,36 468,16 0,16" fill="var(--red)"/>
      <polygon points="0,22 480,22 520,62 0,62" fill="var(--red)"/>
      <polygon points="500,42 540,42 540,62 520,62" fill="var(--red)"/>
    </svg>
    <p class="address">487 North Corwin Parkway Suite 260, Marlow Springs, FL 33127</p>
  </section>
</main>
</body>
</html>
```